High end cable company busines card and letterhead

Dear designers,
We assemble high end audio cables that cost a couple of hundred dollars per piece and we are improving the looks of the product.
When people buy a cable they get a leather pouch with the invoice (letterhead) , a business card of the maker and also a quality control card  / warranty card.
The quality control card  is the same size as a business card and the back of the quality control card is the same back as the business card. So we need 4 things:
-1 back of a business card
-1 front of a business card (a file where we can change the name and details of the worker)
-1 quality control front (I will add a photo of an example)
-1 letterhead
We want to make letterpress business cards and use shiny foil for the logo’s. We like the colors black and copper or black and gold for the back. The front of the business card can also be black, copper and white but it does not have to be those colors. We want people to have the feeling that they bought something expensive and high quality.
The front of the quality control card has to be white so we can check things off with a sharpie / pen.
What has to be on the cards:
Business card:
- Our Logo
-Text: Meet the maker (people get the business card of the one who made the cable)
-Name
-Address
-Website (www.tallowfenwire.com)
-Email address
-Text: For any advise or questions about your cable feel free to contact me.
What has to be on the quality control card:
-Our logo
-Text: quality controll and warranty card (small at the bottom)
-text:
Assembled by:________________
Date: ______-______-____________
QC by:_________________________

Assembly QC [   ]
Measurement QC [   ]
Aesthetics [   ]
(The box [    ] is for the initials of the person that does the QC, it can also be a line or something else)
The letterhead can be your own idea as long as it looks luxurious.
You can download our logo. We have a black one and gold / black but you can change the Color to Match your design. (For instance copper or something) There is also a white one that can be used with the icon on the left.
Some links of stuff we like:
-https://clipvault.example/Kq3rLm8zXa1 (The looks of this card maybe a bit less busy looking)
-https://b.brindlemart.example/_pRxwQaf
-https://b.brindlemart.example/_pTj4Wob
-https://b.brindlemart.example/_pYeuZ11

```html
<!DOCTYPE html>
<html lang="en">
<head>
<meta charset="utf-8">
<title>Tallowfen Wire Letterhead</title>
<link rel="stylesheet" href="https://fonts.googleapis.com/css2?family=Montserrat:wght@400;500&display=swap">
<style>
  :root {
    --backdrop: #e9e9e9;
    --paper: #f7f7f6;
    --band: #2a2629;
    --gold-deep: #c9981f;
    --gold-bright: #ecc52a;
    --ink: #2b2b2b;
    --ink-soft: #4a4a4a;
    --signature-tone: #2238a8;
  }
  * { box-sizing: border-box; margin: 0; padding: 0; }
  html, body {
    width: 1200px;
    height: 900px;
    overflow: hidden;
    background: var(--backdrop);
  }
  .letterhead {
    position: absolute;
    left: 296px;
    top: 20px;
    width: 608px;
    height: 860px;
    background: var(--paper);
    box-shadow: 0 2px 10px rgba(0,0,0,0.12);
    font-family: "Montserrat", sans-serif;
    color: var(--ink);
    overflow: hidden;
  }
  .side-band {
    position: absolute;
    left: 0;
    top: 0;
    width: 128px;
    height: 100%;
    background: var(--band);
  }
  .side-band__stripe {
    position: absolute;
    left: 128px;
    top: 0;
    width: 12px;
    height: 100%;
    background: linear-gradient(180deg, var(--gold-deep), var(--gold-bright) 55%, var(--gold-deep));
  }
  .side-band__mark {
    position: absolute;
    left: 44px;
    top: 52px;
    width: 40px;
    height: 40px;
    background: var(--gold-bright);
  }
  .wordmark {
    position: absolute;
    left: 168px;
    top: 60px;
    font-size: 17px;
    font-weight: 400;
    letter-spacing: 0.32em;
    color: var(--ink);
    line-height: 1.2;
  }
  .sender-address {
    position: absolute;
    right: 40px;
    top: 36px;
    font-size: 8px;
    line-height: 1.45;
    color: var(--ink-soft);
    text-align: left;
  }
  .letter-body {
    position: absolute;
    left: 250px;
    top: 292px;
    width: 312px;
    font-size: 8.6px;
    line-height: 1.42;
    color: var(--ink);
    text-align: justify;
  }
  .letter-body p + p { margin-top: 11px; }
  .sign-off {
    position: absolute;
    left: 250px;
    top: 640px;
  }
  .sign-off__signature {
    display: block;
    width: 150px;
    height: 30px;
    border-radius: 15px;
    background: linear-gradient(90deg, rgba(34,56,168,0.18), rgba(34,56,168,0.06));
  }
  .sign-off__role {
    margin-top: 4px;
    font-size: 9px;
    color: var(--ink);
  }
</style>
</head>
<body>
  <main class="letterhead">
    <div class="side-band">
      <div class="side-band__mark"></div>
    </div>
    <div class="side-band__stripe"></div>

    <div class="wordmark">TALLOWFEN<br>WIRE</div>

    <address class="sender-address" style="font-style:normal">
      48 Marrow Lane, Eastbridge<br>
      Vermont 05221<br>
      www.tallowfenwire.com
    </address>

    <section class="letter-body">
      <p>Letterhead samples are a great way of deciding what kind of letterhead you want to design for you and your company. The internet has a ton of great letterhead samples to browse through. Whether you want something simple, with just a couple lines of text of your business information, or something decorative and stunning, with photos and logos on the top and bottom of the page, it will be easy to find what you want, because there are samples online for basically any type of letterhead you could want.</p>
      <p>Any business could easily benefit from browsing through some letterhead samples if only to get an idea for what kind of letterhead their company might want. Letterheads are just one of the tools that a business professional could use to help increase their customer base, and to really be memorable to everyone they write a letter to. Letterhead is such an effective tool for marketing and advertising, but because it's quite a simple and well known idea, it is often unfairly overlooked. Make sure you don't make that mistake, and make some letterhead samples of your own today.</p>
      <p>Whether you want to get new customers to remember you and become part of your clientele, or you just want to send out friendly reminders to your existing clients, customizing your own letterhead samples can really help you out. Try out some letterhead samples and you will not regret it, and I'm sure you will add a new tool to your business' arsenal of networking, marketing, and advertising tools.</p>
    </section>

    <div class="sign-off">
      <span class="sign-off__signature" role="img" aria-label="Handwritten signature of Elias Thornbury in blue ink"></span>
      <p class="sign-off__role">company director</p>
    </div>
  </main>
</body>
</html>
```